R. K. Dalby, CPA & Associates, LLC
Your Accounting, Finance, and Tax Specialist
R. K. Dalby, CPA & Associates, LLC -
Use specific fonts
open to fonts
Professional
Rennick K. Dalby, CPA
President
4718 Copper Wren Ave. West Palm Beach, FL 33952
rennickdalbycpa@mailnook.test

```html
<!DOCTYPE html>
<html lang="en">
<head>
<meta charset="utf-8">
<title>R. K. Dalby, CPA &amp; Associates, LLC — Business Cards</title>
<link rel="stylesheet" href="https://fonts.googleapis.com/css2?family=Tinos:ital,wght@0,400;0,700;1,400&display=swap">
<style>
  :root{
    --stage:#ece9e6;
    --paper:#ffffff;
    --ink:#2b2b2b;
    --plum:#6b2f5f;
    --magenta:#a3267f;
    --magenta-dark:#7c1b60;
    --grey:#8d8d8d;
    --grey-light:#c9c9c9;
    --night:#0e0e0e;
    --night-ink:#e9e9e9;
  }
  *{box-sizing:border-box;margin:0;padding:0}
  html,body{width:1200px;height:852px;overflow:hidden;background:var(--stage)}
  body{position:relative;font-family:"Tinos",serif;color:var(--ink)}

  .card{position:absolute;width:620px;height:354px;border-radius:18px;overflow:hidden;
        background:var(--paper);box-shadow:0 6px 18px rgba(0,0,0,.18)}
  .card--light{left:90px;top:70px}
  .card--dark{left:490px;top:428px;background:var(--night);color:var(--night-ink)}

  .brand{position:absolute;left:40px;top:44px;display:flex;align-items:center}
  .brand__mark{width:72px;height:72px;border-radius:50%;border:4px solid var(--magenta);flex:none}
  .brand__rule{width:1px;height:110px;background:var(--grey);margin:0 16px 0 28px}
  .brand__name{font-weight:400;color:var(--plum);line-height:1}
  .card--dark .brand__name{color:var(--night-ink)}
  .brand__line1{display:block;font-size:38px;letter-spacing:.5px}
  .brand__line2{display:block;font-size:24px;margin-top:4px}
  .tagline{position:absolute;left:181px;top:138px;font-size:12.5px;font-style:italic;color:var(--magenta)}

  .person{position:absolute;left:40px;top:188px}
  .person__name{font-size:20px;font-weight:700;color:var(--magenta)}
  .person__title{font-size:14px;font-style:italic;margin-left:118px;margin-top:2px}
  .person__address{font-size:15px;line-height:1.35;margin-top:12px;margin-left:52px}

  .contact{position:absolute;left:370px;top:190px;list-style:none;font-size:15px}
  .contact li{display:flex;align-items:center;height:24px}
  .contact svg{width:14px;height:14px;margin-right:10px;fill:var(--magenta)}

  .swoosh{position:absolute;left:0;bottom:0;width:620px;height:80px}
</style>
</head>
<body>

<section class="card card--light" aria-label="Business card, light version">
  <div class="brand">
    <span class="brand__mark"></span>
    <span class="brand__rule"></span>
    <span class="brand__name"><span class="brand__line1">R. K. DALBY</span><span class="brand__line2">CPA &amp; Associates, LLC</span></span>
  </div>
  <p class="tagline">Your Accounting, Finance, and Tax Specialist</p>
  <div class="person">
    <p class="person__name">Rennick K. Dalby, CPA</p>
    <p class="person__title">President</p>
    <p class="person__address">4718 Copper Wren Ave.<br>West Palm Beach, FL 33952</p>
  </div>
  <ul class="contact">
    <li><svg viewBox="0 0 14 14"><rect x="3" y="0" width="8" height="14" rx="1.5"/></svg>561.555.0173</li>
    <li><svg viewBox="0 0 14 14"><rect x="0" y="5" width="14" height="9" rx="1"/><rect x="3" y="0" width="8" height="5"/></svg>561.555.0148</li>
    <li><svg viewBox="0 0 14 14"><circle cx="7" cy="7" r="6.5"/></svg>rennickdalbycpa@mailnook.test</li>
  </ul>
  <svg class="swoosh" viewBox="0 0 620 80" preserveAspectRatio="none" aria-hidden="true">
    <path d="M0 40 Q310 0 620 22 L620 36 Q310 14 0 54Z" fill="var(--grey-light)"/>
    <path d="M0 56 Q310 18 620 38 L620 80 L0 80Z" fill="var(--magenta)"/>
    <path d="M0 70 Q310 40 620 58 L620 80 L0 80Z" fill="var(--magenta-dark)"/>
  </svg>
</section>

<section class="card card--dark" aria-label="Business card, dark version">
  <div class="brand">
    <span class="brand__mark"></span>
    <span class="brand__rule"></span>
    <span class="brand__name"><span class="brand__line1">R. K. DALBY</span><span class="brand__line2">CPA &amp; Associates, LLC</span></span>
  </div>
  <p class="tagline">Your Accounting, Finance, and Tax Specialist</p>
  <div class="person">
    <p class="person__name">Rennick K. Dalby, CPA</p>
    <p class="person__title">President</p>
    <p class="person__address">4718 Copper Wren Ave.<br>West Palm Beach, FL 33952</p>
  </div>
  <ul class="contact">
    <li><svg viewBox="0 0 14 14"><rect x="3" y="0" width="8" height="14" rx="1.5"/></svg>561.555.0173</li>
    <li><svg viewBox="0 0 14 14"><rect x="0" y="5" width="14" height="9" rx="1"/><rect x="3" y="0" width="8" height="5"/></svg>561.555.0148</li>
    <li><svg viewBox="0 0 14 14"><circle cx="7" cy="7" r="6.5"/></svg>rennickdalbycpa@mailnook.test</li>
  </ul>
  <svg class="swoosh" viewBox="0 0 620 80" preserveAspectRatio="none" aria-hidden="true">
    <path d="M0 40 Q310 0 620 22 L620 36 Q310 14 0 54Z" fill="var(--grey)"/>
    <path d="M0 56 Q310 18 620 38 L620 80 L0 80Z" fill="var(--magenta)"/>
    <path d="M0 70 Q310 40 620 58 L620 80 L0 80Z" fill="var(--magenta-dark)"/>
  </svg>
</section>

</body>
</html>
```